Wordpress Design for Software Company

I have a website that is not developed in WordPress. I need the current site www.mirtawel.com/projects/plumvane to be redesigned in Wordpress. I would to keep some of the look and feel but change other things.
1) such as logo background color
2) have (3) columns in on inner pages
3) so nice pictures or graphic layouts I am hoping that you will be able to improve on the look of the website.
Target Market(s)
B2B Companies that deploy call centers or have inside sales staff.
Industry/Entity Type
It Company
Look and feel

```html
<!DOCTYPE html>
<html lang="en">
<head>
<meta charset="utf-8">
<title>Plumvane – Call Center Solutions</title>
<link rel="stylesheet" href="https://fonts.googleapis.com/css2?family=Source+Sans+3:wght@400;600&family=Roboto:wght@300;400;700&family=Roboto+Condensed:wght@700&family=Noto+Serif:wght@700&display=swap">
<style>
:root{
  --brand-blue:#1c5f9f;
  --brand-orange:#e8661c;
  --accent-gold:#f4b21f;
  --accent-gold-light:#fcd451;
  --tab-blue:#1e6ea9;
  --tab-blue-light:#3b8fc9;
  --text-gray:#5d5d5d;
  --link-gray:#777;
  --panel-border:#e2e2e2;
  --footer-bg:#eef3f8;
  --footer-navy:#14336a;
  --contact-cyan:#bfeefb;
  --contact-border:#5cc3e3;
  --page-warm:#fbeccd;
}
*{box-sizing:border-box;margin:0;padding:0}
html,body{width:1082px;height:1200px;overflow:hidden}
body{background:#fff;font-family:"Roboto",Tahoma,sans-serif;color:var(--text-gray)}
.page{position:absolute;left:0;top:0;width:1024px;height:1136px;transform:scale(1.0566);transform-origin:0 0;
  background:radial-gradient(ellipse at 50% -10%,var(--page-warm) 0%,#fdf6e8 40%,#fff 75%)}
.abs{position:absolute}
.logo{left:47px;top:52px;display:flex;align-items:center;gap:12px}
.logo-mark{width:30px;height:30px;border-radius:50%;background:var(--brand-orange)}
.logo-name{font-family:"Source Sans 3",sans-serif;font-size:32px;font-weight:400;color:var(--brand-blue)}
.btn-tool{height:24px;border:1px solid #d9d2c4;border-radius:3px;background:linear-gradient(#fff,#ece8e1);
  font-family:"Source Sans 3",sans-serif;font-size:14px;color:var(--brand-orange);display:flex;align-items:center;justify-content:center;gap:5px}
.caret{width:0;height:0;border-left:4px solid transparent;border-right:4px solid transparent;border-top:5px solid var(--brand-orange)}
.search-field{left:704px;top:68px;width:202px;height:24px;border:1px solid #d6d0c6;border-radius:4px;background:#fff}
.nav-item{top:114px;height:32px;border:1px solid #d7d2ca;border-radius:3px;background:linear-gradient(#fff,#e9e6e1);
  font-family:"Source Sans 3",sans-serif;font-size:17px;color:var(--brand-orange);display:flex;align-items:center;justify-content:center;gap:8px;box-shadow:0 1px 2px rgba(0,0,0,.12)}
.nav-item .caret{border-left-width:5px;border-right-width:5px;border-top-width:7px}
.main-frame{left:19px;top:156px;width:985px;height:956px;background:#fff;border:1px solid var(--panel-border);border-radius:8px;box-shadow:0 0 4px rgba(0,0,0,.06)}
.card{background:#fff;border:1px solid var(--panel-border);border-radius:6px;overflow:hidden}
.hero{left:30px;top:167px;width:686px;height:294px}
.hero-photo{position:absolute;inset:0;background:linear-gradient(90deg,#6f7a86 0%,#a9b2bc 35%,#d3d8de 65%,#fff 85%)}
.hero-title{position:absolute;left:363px;top:198px;font-family:"Roboto Condensed",sans-serif;font-weight:700;font-size:26px;color:var(--brand-orange);letter-spacing:-.5px;text-shadow:0 0 3px #fff}
.hero-btn{position:absolute;left:532px;top:239px;width:138px;height:29px;border:1px solid #d39a10;border-radius:5px;
  background:linear-gradient(var(--accent-gold-light),var(--accent-gold));font-size:16px;color:#333;display:flex;align-items:center;justify-content:center}
.side-card{left:730px;width:261px}
.side-head{height:43px;background:linear-gradient(#fcd65a,var(--accent-gold));display:flex;align-items:center;gap:8px;padding-left:10px;
  font-family:"Roboto Condensed",sans-serif;font-weight:700;font-size:21px;color:#fff;text-shadow:0 1px 1px rgba(150,90,0,.5)}
.side-head .dot{width:24px;height:18px;border-radius:50%;background:#7a5410}
.bullet-list{list-style:none;padding:14px 14px 0 6px}
.bullet-list li{position:relative;padding-left:15px;font-size:12px;line-height:17px;color:var(--link-gray);margin-bottom:7px;letter-spacing:.2px}
.bullet-list li::before{content:"";position:absolute;left:0;top:4px;width:8px;height:8px;background:var(--accent-gold);border-radius:1px}
.bullet-list li::after{content:"";position:absolute;left:3px;top:6px;border-left:3px solid #fff;border-top:2px solid transparent;border-bottom:2px solid transparent}
.learn-more{position:absolute;right:19px;bottom:15px;font-size:11px;color:#223b6f;text-decoration:underline}
.about{left:30px;top:475px;width:687px;height:349px}
.tab-bar{height:43px;background:linear-gradient(var(--tab-blue-light),var(--tab-blue));display:flex}
.tab{color:#fff;font-size:14px;display:flex;align-items:center;padding:0 17px;border-right:1px solid #4f9fd4}
.about-title{position:absolute;left:13px;top:61px;font-size:14px;color:var(--tab-blue)}
.about-text{position:absolute;left:13px;top:92px;width:440px;font-size:12px;line-height:18px;font-weight:300;color:var(--text-gray)}
.about-text b{font-weight:700}
.about-text p+p{margin-top:18px}
.about-photo{position:absolute;left:476px;top:92px;width:194px;height:209px;border-radius:6px;
  background:linear-gradient(160deg,#2a4f86 0%,#5f7fa6 45%,#c9a98c 80%,#e9ddd2 100%);box-shadow:0 1px 3px rgba(0,0,0,.3)}
.links-card{top:475px;height:349px}
.contact-box{position:absolute;left:9px;top:173px;width:242px;height:101px;border:1px solid var(--contact-border);border-radius:5px;background:linear-gradient(#d6f6fd,var(--contact-cyan))}
.contact-phone{position:absolute;left:51px;top:10px;font-family:Arial,sans-serif;font-size:24px;color:#111}
.contact-toll{position:absolute;left:56px;top:36px;font-family:Arial,sans-serif;font-size:12px;color:#111}
.contact-mail{position:absolute;left:51px;top:64px;font-family:Arial,sans-serif;font-size:14px;color:#111}
.social{position:absolute;top:285px;width:119px;height:42px;display:flex;align-items:center;gap:8px;padding-left:4px;color:#fff;font-size:12px;font-weight:700;line-height:14px;text-align:center}
.social .square{width:28px;height:28px;background:rgba(255,255,255,.85);flex:none}
.social-a{left:9px;background:linear-gradient(#3e5b9a,#2c4682)}
.social-b{left:132px;background:linear-gradient(#a9e2f5,#5dc4e8)}
.footer{left:30px;top:838px;width:961px;height:262px;background:var(--footer-bg);border:1px solid #e3e8ee;border-radius:6px}
.foot-col{position:absolute;top:24px}
.foot-col+.foot-col{border-left:1px solid #dfe6ee}
.foot-col h4{font-family:"Noto Serif",serif;font-size:14px;color:var(--footer-navy);margin-bottom:8px}
.foot-col ul{list-style:none}
.foot-col li{position:relative;padding-left:15px;font-size:11px;line-height:14px;color:#222;margin-bottom:10px}
.foot-col li::before{content:"";position:absolute;left:3px;top:3px;border-left:4px solid #2348a0;border-top:3px solid transparent;border-bottom:3px solid transparent}
.copyright{position:absolute;right:15px;bottom:13px;font-size:11px;color:#14336a}
</style>
</head>
<body>
<div class="page">
  <div class="abs logo"><span class="logo-mark"></span><span class="logo-name">Plumvane</span></div>

  <div class="abs btn-tool" style="left:622px;top:68px;width:77px">Login <span class="caret"></span></div>
  <div class="abs search-field"></div>
  <div class="abs btn-tool" style="left:910px;top:68px;width:77px">Search<span class="caret"></span></div>

  <nav>
    <div class="abs nav-item" style="left:466px;width:125px">PRODUCTS <span class="caret"></span></div>
    <div class="abs nav-item" style="left:599px;width:127px">SOLUTIONS <span class="caret"></span></div>
    <div class="abs nav-item" style="left:733px;width:133px">RESOURCES <span class="caret"></span></div>
    <div class="abs nav-item" style="left:873px;width:116px">SERVICES <span class="caret"></span></div>
  </nav>

  <div class="abs main-frame"></div>

  <section class="abs card hero">
    <div class="hero-photo" role="img" aria-label="Call center agents wearing headsets at their desks"></div>
    <div class="hero-title">Lorem Ipsum Dolor Sit amet</div>
    <div class="hero-btn">Know More</div>
  </section>

  <aside class="abs card side-card" style="top:167px;height:294px">
    <div class="side-head"><span class="dot"></span>Whats New</div>
    <ul class="bullet-list">
      <li>Remote IP Agent/Virtual Agent</li>
      <li>Plumvane and Veltrion Channel</li>
      <li>Network Partner Corvale Net Communi-cation Provide a "Universal Phone" Solution to NY based Mortgage Finance Company</li>
      <li>Find out what people are saying about the Plumvane Hosted Predictive Dialer System</li>
      <li>More Press</li>
    </ul>
    <span class="learn-more">Learn More</span>
  </aside>

  <section class="abs card about">
    <div class="tab-bar">
      <div class="tab">Who We Are</div>
      <div class="tab" style="padding:0 20px">What We Do</div>
      <div class="tab">Our Clients</div>
      <div class="tab" style="border:0">Try Us Out</div>
    </div>
    <h2 class="about-title" style="font-weight:400">About Plumvane Corporation</h2>
    <div class="about-text">
      <p>Practical <b>call center solutions</b> for the contact center industry<br>Plumvane is an industry-leader in the development of call center solutions and predictive dialers for industry-specific applications ranging from financial services to home remodeling and other related companies that utilize the services of Predictive Dialing and Contact Center Management &amp; Customer Interaction. We offer both premise based and hosted solutions to small to medium-sized inside sales organizations to larger call centers.</p>
      <p>Our goal is to provide a seamless cost effective call center solutions which involves the cohesive blend of computer telephony integration (CTI) applica-tions, web centric applications, customer relationship (CRM), agent interaction and other channels of communications such as web call back, web chat, email, fax and web collaboration</p>
    </div>
    <div class="about-photo" role="img" aria-label="Two smiling business colleagues in front of an office building"></div>
  </section>

  <aside class="abs card side-card links-card">
    <div class="side-head"><span class="dot"></span>Important Links</div>
    <ul class="bullet-list">
      <li>Products</li>
      <li>Hosted Applications</li>
      <li>INtegrating Dialing Solutions</li>
      <li>Industry Specific Solutions</li>
    </ul>
    <div class="contact-box">
      <svg class="abs" style="left:15px;top:12px" width="22" height="24" viewBox="0 0 22 24"><path d="M5 2 L9 7 L7 10 Q9 15 13 18 L16 16 L20 20 L17 23 Q8 22 3 12 Q1 6 5 2Z" fill="#d9302a"/></svg>
      <div class="contact-phone">1.888.555.0142</div>
      <div class="contact-toll">(Toll FREE)</div>
      <svg class="abs" style="left:18px;top:66px" width="20" height="14" viewBox="0 0 20 14"><rect x="0.5" y="0.5" width="19" height="13" fill="#f6c12a" stroke="#c98f0a"/><path d="M1 1 L10 8 L19 1" fill="none" stroke="#c98f0a"/></svg>
      <div class="contact-mail">sales@plumvanecorp.com</div>
    </div>
    <div class="social social-a"><span class="square"></span><span>Join Us On<br>Linkbook</span></div>
    <div class="social social-b"><span class="square"></span><span>Follow Us On<br>Chirper</span></div>
  </aside>

  <footer class="abs footer">
    <div class="foot-col" style="left:21px;width:280px">
      <h4>Products</h4>
      <ul>
        <li>Hosted Predictive Dialer</li>
        <li>Inbound/Outbound Blended Dialer &amp; ACD</li>
        <li>CallStation™ Premise Based Predictive Dialer</li>
        <li>Contact Manager CRM</li>
        <li>Auto, Preview and Progressive Dialing</li>
        <li>IVR/Power Voice</li>
        <li>Digital Call Recording</li>
      </ul>
    </div>
    <div class="foot-col" style="left:301px;width:203px;padding-left:51px;height:200px">
      <h4>Solutions</h4>
      <ul>
        <li>Hosted Solutions</li>
        <li>Premise Based</li>
        <li>Industry Specific</li>
        <li>Small Office</li>
        <li>Mid Size</li>
        <li>Enterprise</li>
      </ul>
    </div>
    <div class="foot-col" style="left:504px;width:209px;padding-left:50px;height:200px">
      <h4>Resources</h4>
      <ul>
        <li>Applications</li>
        <li>Resources Link 2</li>
      </ul>
    </div>
    <div class="foot-col" style="left:713px;width:220px;padding-left:51px;height:200px">
      <h4>Services</h4>
      <ul>
        <li>Technical Support</li>
        <li>Consulting &amp; Programming</li>
        <li>Telecom Services - PBX</li>
      </ul>
    </div>
    <div class="copyright">© 2011 plumvanecorp.com. All Rights Reserved.</div>
  </footer>
</div>
</body>
</html>
```